Business Card Design

New business card design

Target Market(s)

Residential & Commercial Property Managers

Industry/Entity Type

Plumbing Services

Contact Information for Business Card

Name - Owen Tredgold, title - Director, Phone Number - 0431 862 507, email - owen@rvb-plumbing.com.au, Company ABN - 73 215 904 386,

Font styles to use
Sans Serif

Colors
0054AA
0677BA
7BADD7
CADEEF
E8F1F8

```html
<!DOCTYPE html>
<html lang="en">
<head>
<meta charset="utf-8">
<title>RVB Plumbing Services – Business Card</title>
<link rel="stylesheet" href="https://fonts.googleapis.com/css2?family=Montserrat:wght@400;500;600;700&family=Ubuntu:wght@400;500;700&display=swap">
<style>
  :root {
    --backdrop: #9a9a9a;
    --card: #ffffff;
    --water: #00adec;
    --ink: #1f2329;
    --muted: #555a60;
    --band: #000000;
  }
  * { box-sizing: border-box; margin: 0; padding: 0; }
  html, body { width: 1074px; height: 1200px; overflow: hidden; }
  body { background: var(--backdrop); position: relative; font-family: "Montserrat", sans-serif; }

  .card {
    position: absolute;
    width: 609px;
    height: 348px;
    background: var(--card);
    overflow: hidden;
  }
  .card--front { left: 228px; top: 162px; }
  .card--back  { left: 232px; top: 660px; }

  .wordmark { position: absolute; color: var(--ink); font-family: "Montserrat", sans-serif; font-weight: 500; }
  .wordmark__name { display: block; line-height: 1; letter-spacing: 2px; }
  .wordmark__tag { display: block; text-transform: lowercase; white-space: nowrap; }
  .wordmark__dot { display: inline-block; border-radius: 50%; background: var(--water); vertical-align: middle; }

  .card--front .wordmark { left: 60px; top: 146px; width: 250px; text-align: center; }
  .card--front .wordmark__name { font-size: 62px; }
  .card--front .wordmark__dot { width: 14px; height: 14px; margin-left: 6px; }
  .card--front .wordmark__tag { font-size: 10px; letter-spacing: 8.2px; margin-top: 12px; }

  .water-panel { position: absolute; left: 330px; top: 0; width: 279px; height: 348px; background: var(--water); }

  .card--back .wordmark { left: 58px; top: 70px; width: 168px; text-align: center; }
  .card--back .wordmark__name { font-size: 42px; }
  .card--back .wordmark__dot { width: 10px; height: 10px; margin-left: 4px; }
  .card--back .wordmark__tag { font-size: 7px; letter-spacing: 5.3px; margin-top: 8px; }

  .person { position: absolute; left: 335px; top: 75px; padding-left: 12px; border-left: 5px solid var(--band); height: 46px; }
  .person__name { font-family: "Ubuntu", sans-serif; font-weight: 500; font-size: 26px; line-height: 26px; color: var(--water); margin-top: -2px; }
  .person__title { font-family: "Ubuntu", sans-serif; font-weight: 400; font-size: 16px; line-height: 18px; color: var(--water); padding-left: 4px; }

  .contact { position: absolute; left: 34px; top: 212px; list-style: none; }
  .contact__item { display: flex; align-items: center; height: 18px; margin-bottom: 8px; color: var(--water); font-weight: 600; font-size: 14px; letter-spacing: 0.4px; }
  .contact__icon { width: 16px; height: 16px; margin-right: 15px; flex: none; }

  .abn-band {
    position: absolute; left: 0; top: 293px; width: 609px; height: 32px;
    background: var(--band); color: #ffffff; font-weight: 600; font-size: 15px;
    letter-spacing: 2.4px; text-align: center; line-height: 32px;
  }
</style>
</head>
<body>

  <section class="card card--front" aria-label="Business card front">
    <div class="wordmark">
      <span class="wordmark__name">rvb<span class="wordmark__dot"></span></span>
      <span class="wordmark__tag">plumbing services</span>
    </div>
    <div class="water-panel" role="img" aria-label="Large blue brand decoration area"></div>
  </section>

  <section class="card card--back" aria-label="Business card back">
    <div class="wordmark">
      <span class="wordmark__name">rvb<span class="wordmark__dot"></span></span>
      <span class="wordmark__tag">plumbing services</span>
    </div>

    <div class="person">
      <p class="person__name">Owen Tredgold</p>
      <p class="person__title">Director</p>
    </div>

    <ul class="contact">
      <li class="contact__item">
        <svg class="contact__icon" viewBox="0 0 16 16" aria-hidden="true">
          <circle cx="8" cy="8" r="8" fill="var(--water)"/>
          <path d="M5.3 4.2c.4-.3.8-.2 1 .2l.7 1.3c.2.4.1.7-.2.9l-.4.3c.4.9 1.1 1.7 2 2.1l.3-.4c.2-.3.6-.4.9-.2l1.3.7c.4.2.5.6.2 1-.5.8-1.3 1.1-2.2.7-2-.9-3.4-2.4-4.2-4.3-.3-.9 0-1.7.6-2.3z" fill="#fff"/>
        </svg>
        <span>0431 862 507</span>
      </li>
      <li class="contact__item">
        <svg class="contact__icon" viewBox="0 0 16 16" aria-hidden="true">
          <circle cx="8" cy="8" r="8" fill="var(--water)"/>
          <rect x="4" y="5.2" width="8" height="5.6" rx="0.6" fill="#fff"/>
          <path d="M4.3 5.5 8 8.4l3.7-2.9" fill="none" stroke="var(--water)" stroke-width="0.9"/>
        </svg>
        <span>owen@rvb-plumbing.com.au</span>
      </li>
    </ul>

    <div class="abn-band">ABN - 73 215 904 386</div>
  </section>

</body>
</html>
```